Brochure Design Project

We are a payroll company. We offer a wide variety of products and services:
1. Payroll Processing
2. Employee Direct Deposit
3. Time and attendance
4. HR services
5. Employee Employee Benefits

I'd like to develop a one page template that uses a combination of our logo (attached), colors (attached) and possible a picture. The picture could be shown as an option as it may change based on the product or service.

Target Market(s)

Adults in the United States ages 22-50. Typically these people are accountants, human resource professionals or entrepreneurs. The payroll industry is dominated by 3 large payroll processors, QLM, Wendrafy and Tolvarex. These companies are very impersonal and make it difficult to resolve issues when they arise. We have grown to over 400 clients by being the opposite of the big guys,

Industry/Entity Type

It Company

Font styles to use
Sans Serif

Requirements
Must have
• The brochure can be one or two pages.
Nice to have
• I'll know it when I see it but I can't describe it. I have attached a few brochures that have caught my eye.
Should not have
• No cartoons. No money signs. Hip, new, fresh are words I'd use to describe the winning product. Of the three people I described in my target market, the entrepreneur is the market I'd most like to target.

```html
<!DOCTYPE html>
<html lang="en">
<head>
<meta charset="utf-8">
<title>Paystead Partners — Brochure</title>
<link href="https://fonts.googleapis.com/css2?family=Arimo:wght@400;700&display=swap" rel="stylesheet">
<style>
  :root {
    --navy: #1f3470;
    --heading: #2b3c7e;
    --green: #8dc63f;
    --grey: #6d6e70;
    --ink: #111111;
    --paper: #ffffff;
  }
  * { margin: 0; padding: 0; box-sizing: border-box; }
  html, body { width: 831px; height: 1200px; overflow: hidden; background: var(--paper); }
  .brochure {
    position: relative;
    width: 831px;
    height: 1200px;
    overflow: hidden;
    font-family: "Arimo", Arial, sans-serif;
    color: var(--ink);
  }
  .header-wave { position: absolute; top: 0; left: 0; width: 831px; height: 170px; }
  .brand-name {
    position: absolute;
    font-weight: 700;
    color: var(--navy);
    white-space: nowrap;
    letter-spacing: 0.5px;
  }
  .brand-name--top { right: 22px; top: 92px; font-size: 38px; }
  .brand-name--footer { right: 14px; top: 1145px; font-size: 26px; }
  .section { position: absolute; }
  .section h2 {
    font-weight: 400;
    font-size: 19px;
    line-height: 22px;
    color: var(--heading);
  }
  .section p {
    font-size: 16.8px;
    line-height: 22.4px;
  }
  .col-left { left: 31px; width: 360px; }
  .col-right { left: 444px; width: 360px; }
  .full { left: 31px; width: 790px; }
  .feature-photo {
    position: absolute;
    left: 447px; top: 496px;
    width: 341px; height: 216px;
    background: linear-gradient(160deg, #e9ecef 0%, #d5dade 40%, #b7c9d3 65%, #9aa3ab 100%);
  }
  .footer-band { position: absolute; left: 0; }
  .footer-band--grey { top: 1139px; width: 583px; height: 15px; background: var(--grey); }
  .footer-band--green { top: 1159px; width: 583px; height: 16px; background: var(--green); }
  .footer-band--navy { top: 1180px; width: 831px; height: 20px; background: var(--navy); }
</style>
</head>
<body>
<main class="brochure">
  <svg class="header-wave" viewBox="0 0 831 170" aria-hidden="true">
    <path d="M0 0 H831 V48 C690 50 420 80 185 153 C130 132 60 114 0 108 Z" fill="var(--navy)"/>
  </svg>
  <div class="brand-name brand-name--top">Paystead Partners</div>

  <section class="section col-left" style="top:233px">
    <h2>LOREM ISPUM</h2>
    <p>Lorem ipsum dolor sit amet, temporibus<br>liberavisse sed cu, an aliquip equidem<br>principes usu. Ex quas suavitate<br>accusamus pri, natum posse perfecto pri<br>te. Ei eam soluta consectetuer, sumo ferri<br>cum ex. At sed modo numquam epicurei.<br>Ad nemore iriure conclusionemque est.<br>An eos affert dolorum veritus. Sit ad<br>forensibus moderatius, eum an iudicabit<br>liberavisse, per mundi possit ea.</p>
  </section>

  <section class="section col-left" style="top:502px">
    <h2>LOREM ISPUM</h2>
    <p>Noluisse erroribus neglegentur in eam. An<br>vix exerci quaestio, quodsi laboramus per<br>ex, meis fugit eirmod eu nec. Ius cu nulla<br>possit sententiae, mel oratio nemore<br>erroribus ei. Pri qualisque erroribus<br>honestatis eu, habeo scripta oblique mei<br>ex. Dolorum tibique et vix, eam quodsi<br>gloriatur te, ut purto liber vel.</p>
  </section>

  <section class="section col-left" style="top:727px">
    <h2>LOREM ISPUM</h2>
    <p>Noluisse erroribus neglegentur in eam. An<br>vix exerci quaestio, quodsi laboramus per<br>ex, meis fugit eirmod eu nec. Ius cu nulla<br>possit sententiae, mel oratio nemore<br>erroribus ei. Pri qualisque erroribus<br>honestatis eu, habeo scripta oblique mei<br>ex. Dolorum tibique et vix, eam quodsi<br>gloriatur te, ut purto liber vel.</p>
  </section>

  <section class="section col-right" style="top:233px">
    <h2>LOREM ISPUM</h2>
    <p>Lorem ipsum dolor sit amet, temporibus<br>liberavisse sed cu, an aliquip equidem<br>principes usu. Ex quas suavitate<br>accusamus pri, natum posse perfecto pri<br>te. Ei eam soluta consectetuer, sumo ferri<br>cum ex. At sed modo numquam epicurei.<br>Ad nemore iriure conclusionemque est.<br>An eos affert dolorum veritus. Sit ad<br>forensibus moderatius, eum an iudicabit<br>liberavisse, per mundi possit ea.</p>
  </section>

  <div class="feature-photo" role="img" aria-label="Photo of a bright open-plan office with white desks, blue chairs and colourful wall graphics"></div>

  <section class="section col-right" style="top:746px">
    <h2>LOREM ISPUM</h2>
    <p>Noluisse erroribus neglegentur in eam. An<br>vix exerci quaestio, quodsi laboramus per<br>ex, meis fugit eirmod eu nec. Ius cu nulla<br>possit sententiae, mel oratio nemore<br>erroribus ei. Pri qualisque erroribus<br>honestatis eu, habeo scripta oblique mei<br>ex. Dolorum tibique et vix, eam quodsi<br>gloriatur te, ut purto liber vel.</p>
  </section>

  <section class="section full" style="top:965px">
    <h2>LOREM ISPUM</h2>
    <p>Noluisse erroribus neglegentur in eam. An vix exerci quaestio, quodsi laboramus per ex,<br>meis fugit eirmod eu nec. Ius cu nulla possit sententiae, mel oratio nemore erroribus ei. Pri<br>qualisque erroribus honestatis eu, habeo scripta oblique mei ex. Dolorum tibique et vix,<br>eam quodsi gloriatur te, ut purto liber vel.</p>
  </section>

  <div class="footer-band footer-band--grey"></div>
  <div class="footer-band footer-band--green"></div>
  <div class="footer-band footer-band--navy"></div>
  <div class="brand-name brand-name--footer">Paystead Partners</div>
</main>
</body>
</html>
```